Dynamic Business Card for Sports Supplements Company

Hi! I'm looking for an awesome business card to match my existing sports supplement company. I have uploaded my current company logo and screenshot of the front page of my website.

I would like to have something dynamic and interesting and utilize the colors in the website - the reds and purples

The business card should be double sided and focus on a unique eye-catching design on the back and include all the relevant company info.

Most importantly, it should say somewhere: "Sign up on our website for a coupon code."

Target Market(s)

Mostly for women gym goers but it shouldn't be too feminine. It should be in keeping with the website design. It should flow and clearly be connected to it

Industry/Entity Type

Business

Contact Information for Business Card

Lorena K. Vasquez
CEO
LVasquez@Fortivanco.example
www.fortivanco.example
614.275.3081
P.O. Box 48317
Calloway, Ohio 22417

Sign up on our website for a coupon code

Font styles to use
Serif
Sans Serif
Other font styles liked:
• Novecento font family and "Fortivan" is in AR Destine font

Requirements
Must have
• One side should be a bold Fortivan logo design. Even just the symbol itself may be o.k. (see attached file)

```html
<!DOCTYPE html>
<html lang="en">
<head>
<meta charset="utf-8">
<title>Fortivan Business Card</title>
<link rel="stylesheet" href="https://fonts.googleapis.com/css2?family=Oswald:wght@500;600&family=Work+Sans:wght@400;500;600&display=swap">
<style>
  :root {
    --page-bg: #c4c4c4;
    --card-bg: #1f1f1f;
    --card-bg-light: #2a2a2a;
    --ink: #ffffff;
    --ink-soft: #e4e4e4;
    --accent: #d8262c;
    --shadow: rgba(0, 0, 0, 0.35);
  }
  * { box-sizing: border-box; margin: 0; padding: 0; }
  html, body {
    width: 1200px;
    height: 1000px;
    overflow: hidden;
    background: var(--page-bg);
  }
  .canvas {
    width: 1200px;
    height: 1000px;
    display: flex;
    flex-direction: column;
    align-items: center;
    justify-content: center;
    gap: 60px;
  }
  .card {
    position: relative;
    width: 700px;
    height: 400px;
    background: linear-gradient(160deg, var(--card-bg-light) 0%, var(--card-bg) 60%);
    box-shadow: 0 6px 18px var(--shadow);
    color: var(--ink);
  }

  /* Contact side */
  .contact-block {
    position: absolute;
    top: 150px;
    left: 0;
    width: 100%;
    display: flex;
    align-items: center;
  }
  .identity {
    width: 302px;
    text-align: right;
    padding-right: 18px;
  }
  .identity__name {
    font-family: "Oswald", sans-serif;
    font-weight: 500;
    font-size: 25px;
    letter-spacing: 0.5px;
    text-transform: uppercase;
    line-height: 1.1;
  }
  .identity__title {
    font-family: "Oswald", sans-serif;
    font-weight: 500;
    font-size: 14px;
    color: var(--accent);
    letter-spacing: 1px;
    margin-top: 2px;
  }
  .divider {
    width: 2px;
    height: 78px;
    background: var(--accent);
  }
  .details {
    list-style: none;
    padding-left: 18px;
    font-family: "Work Sans", sans-serif;
    font-size: 14px;
    color: var(--ink-soft);
  }
  .details li {
    display: flex;
    align-items: center;
    gap: 10px;
    height: 24px;
  }
  .details svg { width: 14px; height: 14px; flex: none; }
  .details .accent { color: var(--accent); }
  .address {
    position: absolute;
    left: 175px;
    bottom: 34px;
    display: flex;
    align-items: center;
    gap: 10px;
    font-family: "Work Sans", sans-serif;
    font-size: 14px;
    letter-spacing: 0.6px;
    color: var(--ink-soft);
  }
  .address svg { width: 14px; height: 14px; }

  /* Brand side */
  .brand {
    position: absolute;
    top: 128px;
    left: 0;
    width: 100%;
    display: flex;
    flex-direction: column;
    align-items: center;
  }
  .brand__row {
    display: flex;
    align-items: center;
    gap: 14px;
  }
  .brand__mark {
    width: 34px;
    height: 34px;
    background: var(--accent);
  }
  .brand__name {
    font-family: "Oswald", sans-serif;
    font-weight: 600;
    font-size: 48px;
    letter-spacing: 2px;
    text-transform: uppercase;
    color: var(--ink);
    line-height: 1;
  }
  .brand__tagline {
    font-family: "Work Sans", sans-serif;
    font-weight: 500;
    font-size: 14px;
    letter-spacing: 1.5px;
    color: var(--ink-soft);
    margin-top: 10px;
  }
  .coupon {
    position: absolute;
    left: 0;
    bottom: 30px;
    width: 100%;
    text-align: center;
    font-family: "Oswald", sans-serif;
    font-weight: 500;
    font-size: 15px;
    letter-spacing: 1.5px;
    text-transform: uppercase;
    color: var(--ink);
  }
</style>
</head>
<body>
<main class="canvas">

  <section class="card card--contact">
    <div class="contact-block">
      <div class="identity">
        <p class="identity__name">Lorena K. Vasquez</p>
        <p class="identity__title">CEO</p>
      </div>
      <div class="divider"></div>
      <ul class="details">
        <li>
          <svg viewBox="0 0 16 16" aria-hidden="true"><path fill="#d8262c" d="M3.5 1.5l2.5 0 1 3.5-1.8 1.2a8 8 0 0 0 4.6 4.6L11 9l3.5 1v2.5c0 1-1 2-2 2C6.5 14.5 1.5 9.5 1.5 3.5c0-1 1-2 2-2z"/></svg>
          <span>614.275.3081</span>
        </li>
        <li>
          <svg viewBox="0 0 16 16" aria-hidden="true"><rect x="1" y="3" width="14" height="10" fill="#d8262c"/><path d="M1 3l7 6 7-6" fill="none" stroke="#1f1f1f" stroke-width="1.3"/></svg>
          <span>LVasquez@Fortivanco.example</span>
        </li>
        <li>
          <svg viewBox="0 0 16 16" aria-hidden="true"><circle cx="9.5" cy="6.5" r="4.5" fill="none" stroke="#d8262c" stroke-width="2"/><path d="M6.2 9.8L1.5 14.5" stroke="#d8262c" stroke-width="2.4" stroke-linecap="round"/></svg>
          <span>www.<span class="accent">fortivanco</span>.example</span>
        </li>
      </ul>
    </div>
    <p class="address">
      <svg viewBox="0 0 16 16" aria-hidden="true"><path fill="#d8262c" d="M15 1L1 7l5 2 2 6z"/></svg>
      <span>P.O. Box 48317 Calloway, Ohio 22417</span>
    </p>
  </section>

  <section class="card card--brand">
    <div class="brand">
      <div class="brand__row">
        <span class="brand__mark"></span>
        <span class="brand__name">Fortivan</span>
      </div>
      <p class="brand__tagline">your strength ally</p>
    </div>
    <p class="coupon">Sign up on our website for a coupon code</p>
  </section>

</main>
</body>
</html>
```